PRODUCT Catalog Design Project,Scope-4pages+1 Cover page,Click -http://fldr.xz/K8pwRt

Dear Friends ,
[ FERNO BOX LINK TO DOWNLOAD ALL CONTENT Photos & reference catalog - http://fldr.xz/K8pwRt
We would like to introduce ZORVANE GROUP PVT. LTD, we are into bulk material handling product which normally used in CEMENT,STEEL,PHARMA,FOOD Industry, We are looking for a catalog which should be attractive with lots pictures[ According to your design skills ] , FOR .PSD GOOD QUALITY IMAGES PLEASE SENT ME TEST MAIL ON RAHUL.PANTE@ZORVANEGROUP.COM ]
For further information please visit www.zorvanegroup.com

WHAT I WANT FROM YOU: please refer to ferno box link -http://fldr.xz/K8pwRt , i have enclosed some reference catalog picture for understanding color scheme and fonts
There are actual seven pages not properly arranged please find enclosed
First page : it should have very attractive look with product pictures for that i am enclosing each pictures please find enclosed and for description please find word file in which i have arranged data in front of respective picture
Enclosed
1- logo[ If you want to make small changes in logo according to catalog its fine ]
2- word 2010 file in which you will get description with pictures
3- cropped pictures [ if you want .psd format let me know i will provide that if you send me test mail on rahup

now important thing PLEASE SELECT THIS PROJECT only IF YOU REALLY HAVE EXPERIENCE IN INDUSTRIAL CATALOGUE WORK IN PAST
i want very interesting and such catalogue which meets industrial look requirement
Guys i am waiting for best design from you thank you very much for reading HAPPY NEW YEAR

hello every one,

I assure you that we will be give you extra amount of money , if our management team likes your design , we are new to tally hive we are not sure about its working .. 

please visit our website for more further information and description of our product  www.zorvanegroup.com

Reason: We haven't received any new attractive design yet , And we are really hopeful to receive from creative designer

For any photoshop format [.psd ] please send me mail on rahul.pante@zorvanegroup.com , since upload limit is only 30 mb i was not upload it ..Feel free to ask any questions

Thank you 

Reason: we are waiting for best creative design

Dear friends Now this project is committed , since we  are new to tally hive it was not committed but due request from some designers we are doing it right away, we have trust in you ....

Dear friends ,
For all documents, good quality pictures and REFERENCE CATALOG please click on ferno box link below,
These reference catalog just to understand what exactly we are expecting not exactly ,
Fonts -i love tavro products you can used any of font like Lucida Grande, myrid pro , and ya refer to reference for better understanding

FERNO BOX LINK -CLICK  -   http://fldr.xz/K8pwRt

Reason: designs are not as per our expectations.

FONTS -you can use MYRIAD PRO [ tavro product  fonts ] it looks attractive 

Target Market(s)

People who are engineers , managing directors, purchase department managers ..
age group 24 - 65

Industry/Entity Type

Industrial

Requirements
Must have
• ELEGANT COLORS, PLEASE DO NOT USE GOODY COLORS
Nice to have
• colorful lots of shapes please see ferno box link click on that download reference catalog http://fldr.xz/K8pwRt

```html
<!DOCTYPE html>
<html lang="en">
<head>
<meta charset="utf-8">
<title>Zorvane Group — Rotary Airlock Valve Catalogue</title>
<link rel="stylesheet" href="https://fonts.googleapis.com/css2?family=Source+Sans+3:wght@700&display=swap">
<style>
  :root {
    --page-bg: #d9d6d2;
    --ink-black: #000000;
    --band-yellow: #ffe500;
    --red-top: #a3000f;
    --red-mid: #4a0006;
    --red-deep: #170303;
    --brand-red: #c1121c;
    --tile-white: #ffffff;
    --bar-rose: #e9c2b8;
    --text-dark: #1a1010;
    --text-light: #ffffff;
  }
  * { margin: 0; padding: 0; box-sizing: border-box; }
  html, body {
    width: 1200px; height: 960px; overflow: hidden;
    background: var(--page-bg);
    font-family: "Source Sans 3", "Myriad Pro", sans-serif;
  }
  .catalogue-spread {
    position: absolute; left: 20px; top: 70px;
    width: 1160px; height: 819px;
    background: linear-gradient(180deg, var(--red-top) 12%, var(--red-mid) 55%, var(--red-deep) 92%);
    overflow: hidden;
    box-shadow: 0 6px 18px rgba(0,0,0,.35);
  }
  .top-band { position: absolute; left: 0; top: 0; width: 1160px; height: 160px; }
  .bottom-band {
    position: absolute; left: 0; top: 760px; width: 1160px; height: 59px;
    background: var(--ink-black);
    border-top: 14px solid var(--band-yellow);
  }
  .spine {
    position: absolute; left: 580px; top: 112px; width: 1px; height: 648px;
    background: rgba(255,255,255,.85);
  }
  .brand-mark {
    position: absolute;
    width: 153px; height: 47px;
    background: var(--tile-white);
    border: 1px solid #8a8a8a;
    display: flex; align-items: center; justify-content: center;
    text-align: center;
    color: var(--brand-red);
    font-weight: 700; font-size: 18px; line-height: 18px; letter-spacing: .2px;
  }
  .brand-mark--front { left: 612px; top: 24px; }
  .brand-mark--back { left: 208px; top: 406px; }
  .cover-title {
    position: absolute; left: 600px; width: 520px; top: 160px;
    text-align: right;
    color: var(--text-light);
    font-weight: 700; font-size: 42px; letter-spacing: .3px;
    text-shadow: 3px 3px 4px rgba(0,0,0,.8);
  }
  .accent-bar {
    position: absolute; left: 580px; top: 235px; width: 508px; height: 23px;
    background: linear-gradient(90deg, var(--bar-rose) 0%, rgba(200,90,80,.75) 50%, rgba(160,20,20,0) 100%);
  }
  .product-grid { position: absolute; left: 580px; top: 258px; }
  .product-tile {
    position: absolute; width: 127px; height: 127px;
    background: var(--tile-white);
    box-shadow: 3px 4px 6px rgba(0,0,0,.55);
    display: flex; align-items: center; justify-content: center;
  }
  .product-photo {
    width: 96px; height: 66px; border-radius: 6px;
    background: linear-gradient(160deg, #c7ced3 0%, #8b959c 60%, #5d666d 100%);
  }
  .product-photo--blue { background: linear-gradient(160deg, #b6d3dc 0%, #7fa6b4 60%, #4f6f7c 100%); }
  .product-photo--dark { background: linear-gradient(160deg, #9aa0a3 0%, #4c5154 60%, #25292b 100%); }
  .product-photo--pale { background: linear-gradient(160deg, #f2f3f4 0%, #d1d6d9 60%, #a7afb4 100%); }
  .edition-bar {
    position: absolute; left: 653px; top: 724px; width: 507px; height: 36px;
    background: linear-gradient(90deg, rgba(120,10,10,0) 0%, rgba(150,60,55,.8) 35%, var(--bar-rose) 100%);
    display: flex; align-items: center; justify-content: flex-end;
    padding-right: 20px;
    color: var(--text-dark); font-weight: 700; font-size: 19px;
  }
</style>
</head>
<body>
  <main class="catalogue-spread">
    <svg class="top-band" viewBox="0 0 1160 160" aria-hidden="true">
      <path d="M0 50 Q580 142 1160 50 L1160 68 Q580 162 0 68 Z" fill="var(--band-yellow)"/>
      <path d="M0 0 H1160 V54 Q580 146 0 54 Z" fill="var(--ink-black)"/>
    </svg>

    <div class="brand-mark brand-mark--front">ZORVANE<br>GROUP</div>
    <div class="spine"></div>
    <div class="brand-mark brand-mark--back">ZORVANE<br>GROUP</div>

    <h1 class="cover-title">ROTARY AIRLOCK VALVE</h1>
    <div class="accent-bar"></div>

    <section class="product-grid" aria-label="Valve range">
      <div class="product-tile" style="left:0;top:0"><div class="product-photo product-photo--blue" role="img" aria-label="Photo of a blue rotary airlock valve"></div></div>
      <div class="product-tile" style="left:128px;top:0"><div class="product-photo product-photo--pale" role="img" aria-label="Photo of a stainless rotary airlock valve"></div></div>
      <div class="product-tile" style="left:256px;top:0"><div class="product-photo" role="img" aria-label="Photo of a rotary valve with blue geared motor"></div></div>
      <div class="product-tile" style="left:384px;top:0"><div class="product-photo product-photo--pale" role="img" aria-label="Photo of a drop-through rotary valve on a base frame"></div></div>
      <div class="product-tile" style="left:0;top:128px"><div class="product-photo product-photo--blue" role="img" aria-label="Photo of a rotary feeder with side drive"></div></div>
      <div class="product-tile" style="left:128px;top:128px"><div class="product-photo product-photo--dark" role="img" aria-label="Photo of a round-flange cast rotary valve"></div></div>
      <div class="product-tile" style="left:256px;top:128px"><div class="product-photo" role="img" aria-label="Photo of a blow-through rotary valve"></div></div>
      <div class="product-tile" style="left:0;top:256px"><div class="product-photo product-photo--dark" role="img" aria-label="Photo of a heavy duty rotary airlock with motor"></div></div>
      <div class="product-tile" style="left:128px;top:256px"><div class="product-photo product-photo--pale" role="img" aria-label="Photo of a white square-inlet rotary valve"></div></div>
    </section>

    <div class="edition-bar">CATALOGUE 2013</div>
    <div class="bottom-band"></div>
  </main>
</body>
</html>
```